I have an existing corporate logo. I'd like to clean it up bit (sharpen it up) and make it look better (without major redesign). I'd like to get the logo itself in all major file formats for print, web, etc.
Then I'd like a business card design that reflects a strategy consulting firm. It should be clean - logo and text without major graphics, and perhaps some small color treatments that match the logo color. The card should suggest high quality in terms of the company.
I'd like the files for card in all major print formats.
Target Market(s)
Silver Birch Partners is a strategy development and business consulting firm focused on small to mid-sized companies. We specialize in business strategy, comprehensive business plan development, market segmentation and positioning, financial models, marketing and sales strategy, product strategy and the effective use of social media in business growth. We operate as consultants, advisers, retained members of management teams, and Board members. We often serve in the role of Chief Strategy Officer, supporting CEO's and other senior executives to enhance top and bottom line growth.
Our overall approach with clients is to deliver actual results, and we often take an active team role with business founders and management teams to drive business growth and affect real changes in performance. As a result, we approach each situation uniquely and partner with clients in a manner that will have the biggest impact on enterprise value.
Industry/Entity Type
Business
Look and feel

```html
<!DOCTYPE html>
<html lang="en">
<head>
<meta charset="utf-8">
<title>Silver Birch Partners – Business Card</title>
<link href="https://fonts.googleapis.com/css2?family=Arimo:wght@400;700&family=Cinzel:wght@400&display=swap" rel="stylesheet">
<style>
  :root {
    --navy: #22306a;
    --ink: #1d1d1f;
    --black: #0b0b0b;
    --paper: #ffffff;
    --stage: #e9e7e3;
    --rule: #1b1b1b;
  }
  * { box-sizing: border-box; margin: 0; padding: 0; }
  html, body { width: 1200px; height: 858px; overflow: hidden; }
  body {
    background: var(--stage);
    font-family: "Arimo", Arial, sans-serif;
    display: flex; align-items: center; justify-content: center; gap: 50px;
  }
  .card {
    width: 525px; height: 300px; background: var(--paper);
    position: relative; overflow: hidden;
    box-shadow: 0 6px 18px rgba(0,0,0,.18);
  }
  /* Front */
  .front-top { height: 176px; display: flex; align-items: center; justify-content: space-between; padding: 0 28px; gap: 16px; }
  .brand { display: flex; align-items: center; gap: 10px; flex: none; }
  .brand-dot { width: 26px; height: 26px; border-radius: 50%; background: var(--navy); flex: none; }
  .brand-name { font-weight: 700; font-size: 19px; line-height: 1.15; color: var(--ink); text-transform: uppercase; letter-spacing: .4px; white-space: nowrap; }
  .person { text-align: right; flex: none; }
  .person-name { font-family: "Cinzel", Georgia, serif; font-size: 19px; color: var(--ink); letter-spacing: .3px; white-space: nowrap; }
  .person-title { font-size: 13.5px; color: var(--ink); margin-top: 4px; white-space: nowrap; }
  .front-band {
    position: absolute; left: 0; right: 0; bottom: 0; height: 124px;
    background: var(--navy); border-top: 3px solid var(--rule);
    display: flex; justify-content: space-between; align-items: center;
    padding: 0 26px; color: var(--paper); font-size: 12.5px;
  }
  .contact-list { list-style: none; display: grid; gap: 5px; }
  .contact-list li { display: flex; align-items: center; gap: 8px; white-space: nowrap; }
  .contact-list.right li { justify-content: flex-end; }
  .icon { width: 12px; height: 12px; flex: none; }
  .dot-icon { width: 9px; height: 9px; border-radius: 50%; background: var(--paper); flex: none; margin: 0 1.5px; }
  /* Back */
  .back-top { height: 20px; background: var(--black); }
  .back-bottom { position: absolute; left: 0; right: 0; bottom: 0; height: 28px; background: var(--navy); }
  .services { padding: 14px 28px 0 30px; }
  .diamonds { display: flex; gap: 9px; margin-bottom: 6px; }
  .diamonds span { width: 9px; height: 9px; background: var(--black); transform: rotate(45deg); }
  .service-list { list-style: none; font-size: 12.6px; line-height: 1.42; color: var(--ink); }
</style>
</head>
<body>
  <section class="card card-front" aria-label="Business card front">
    <div class="front-top">
      <div class="brand">
        <span class="brand-dot"></span>
        <span class="brand-name">Silver Birch<br>Partners, LLC</span>
      </div>
      <div class="person">
        <p class="person-name">Daniel M. Hartwell</p>
        <p class="person-title">Partner and Founder</p>
      </div>
    </div>
    <div class="front-band">
      <ul class="contact-list">
        <li><svg class="icon" viewBox="0 0 12 12"><rect x="0.5" y="2" width="11" height="8" fill="none" stroke="#fff"/><path d="M0.5 2 6 7 11.5 2" fill="none" stroke="#fff"/></svg>daniel@silverbirchpartners.com</li>
        <li><svg class="icon" viewBox="0 0 12 12"><circle cx="6" cy="6" r="5.3" fill="none" stroke="#fff"/><ellipse cx="6" cy="6" rx="2.3" ry="5.3" fill="none" stroke="#fff"/><path d="M0.7 6h10.6" stroke="#fff"/></svg>silverbirchpartners.com</li>
        <li><span class="dot-icon"></span>silverbirchpartners.com/team/dhartwell/</li>
        <li><span class="dot-icon"></span>@DanHartwell</li>
      </ul>
      <ul class="contact-list right">
        <li>555.014.2290<svg class="icon" viewBox="0 0 12 12"><path d="M2.5 1 4.5 3 3.5 4.5C4.3 6.2 5.8 7.7 7.5 8.5L9 7.5 11 9.5 9.5 11C5 10.5 1.5 7 1 2.5Z" fill="#fff"/></svg></li>
        <li>412 Alder Crest Lane<svg class="icon" viewBox="0 0 12 12"><path d="M6 11.5C3 8 2 6.3 2 4.5a4 4 0 0 1 8 0C10 6.3 9 8 6 11.5Z" fill="#fff"/><circle cx="6" cy="4.5" r="1.5" fill="#22306a"/></svg></li>
        <li>Westbrook, Illinois 60999<span class="icon"></span></li>
      </ul>
    </div>
  </section>

  <section class="card card-back" aria-label="Business card back">
    <div class="back-top"></div>
    <div class="services">
      <div class="diamonds"><span></span><span></span><span></span><span></span></div>
      <ul class="service-list">
        <li>Business strategy development and planning</li>
        <li>Identification of new market opportunities</li>
        <li>Go-to-market strategy</li>
        <li>Marketing and sales strategy</li>
        <li>New business development</li>
        <li>Comprehensive business plan and financial model development</li>
        <li>Strategic market positioning</li>
        <li>Operational turnarounds, improvement and stabilization</li>
        <li>Justification of strategic investments</li>
        <li>Application of technology</li>
        <li>Portfolio analysis - profitability and prioritization</li>
        <li>Insights analysis</li>
      </ul>
    </div>
    <div class="back-bottom"></div>
  </section>
</body>
</html>
```